New IT Consulting Company website - name is Zorvel Consulting

Seeking a new IT Consulting company website in Wordpress, some IT recruitment based skills, about us, services, we have all the content and wireframe details. We then want to build it in Divi ideally

Target Market(s)

IT Consulting companies and also staff augmentation needs

Industry/Entity Type

It Professional

Colors
0355a3

Requirements
Must have
• Home Page,
• Banner (Slider) - What we do
• Banner 2 - Companies / Talent we deal with (Quellbyte, Fendra, TQR, Lumo, Gravelonix etc)
• Our 3 key areas being:
• a) Integration Consulting and Staff Augmentation
• b) Software Development
• c) Data Consulting and Staff Augmentation
• About Data landing page
• About Integration landing page
• Media (news/blog)
• Contact Us
• Then About us - What we Do, How we do it, our values
• Our Solutions Page - Clients landing Page, Candidates landing Page
• Case Studies page
• Blog
• Contact Us
Nice to have
• NA
Should not have
• NA

```html
<!DOCTYPE html>
<html lang="en">
<head>
<meta charset="utf-8">
<title>About Us – Zorvel Consulting</title>
<link href="https://fonts.googleapis.com/css2?family=Ubuntu:wght@500;700&family=Lato:wght@300;400;700&display=swap" rel="stylesheet">
<style>
:root{
  --blue:#2680eb;
  --blue-soft:#e8f1fd;
  --green:#00d68f;
  --ink:#1e1e1e;
  --grey:#7a7a7a;
  --navy:#222d40;
  --line:#e6e6e6;
  --white:#fff;
}
*{margin:0;padding:0;box-sizing:border-box}
html,body{width:1200px;height:2484px;overflow:hidden;background:var(--white)}
body{position:relative;font-family:'Lato',sans-serif;color:var(--grey)}
.abs{position:absolute}
.hero-bg,.cta-bg{position:absolute;left:0;top:0}
.brand{font-family:'Ubuntu',sans-serif;font-weight:700;color:var(--white)}
.site-header .brand{left:88px;top:28px;font-size:27px}
.nav{left:386px;top:38px;display:flex;gap:0;font-size:15px;color:var(--white);align-items:center}
.nav a{color:var(--white);text-decoration:none;margin-right:37px;padding-bottom:6px}
.nav a.active{font-weight:700;border-bottom:2px solid var(--white)}
.nav .cta{position:absolute;left:603px;top:-13px;background:var(--green);font-family:'Ubuntu',sans-serif;font-weight:700;font-size:18px;padding:12px 13px;border-radius:4px;margin:0;border:0;white-space:nowrap}
.page-title{left:0;width:1200px;top:118px;text-align:center;font-family:'Ubuntu',sans-serif;font-weight:700;font-size:58px;color:var(--white)}
.breadcrumb{left:0;width:1200px;top:193px;text-align:center;font-size:15.5px;color:var(--white)}
.breadcrumb svg{vertical-align:-2px;margin-right:10px}
.breadcrumb span.sep{margin:0 12px}
.art{border-radius:18px}
h2.section-title{font-family:'Ubuntu',sans-serif;font-weight:700;font-size:40px;color:var(--ink);letter-spacing:.5px}
.bar{display:block;width:90px;height:7px;background:var(--green);border-radius:4px}
.copy{font-size:15.5px;line-height:25px;color:var(--grey);font-weight:400}
.rule{left:88px;width:1024px;height:1px;background:var(--line)}
.feature{width:190px;text-align:center}
.feature .icon{width:90px;height:90px;border-radius:50%;background:var(--blue-soft);margin:0 auto;display:flex;align-items:center;justify-content:center}
.feature h3{font-family:'Ubuntu',sans-serif;font-weight:500;font-size:17px;color:var(--ink);margin-top:30px}
.feature p{font-size:15px;line-height:22px;margin-top:11px;color:var(--grey)}
.value{left:88px;width:500px;padding-left:48px}
.value svg{position:absolute;left:0;top:2px}
.value h4{font-family:'Ubuntu',sans-serif;font-weight:500;font-size:17px;color:var(--ink)}
.value p{font-size:15.5px;line-height:25px;margin-top:4px}
.cta-title{left:0;width:1200px;top:1906px;text-align:center;font-family:'Ubuntu',sans-serif;font-weight:700;font-size:42px;color:var(--white)}
.cta-text{left:290px;width:620px;top:1988px;text-align:center;font-size:15.5px;line-height:20px;color:#c9ced8}
.btn{left:511px;top:2042px;width:178px;height:46px;background:var(--green);color:var(--white);border-radius:4px;font-family:'Ubuntu',sans-serif;font-weight:700;font-size:18px;display:flex;align-items:center;justify-content:center}
.footer-brand{left:88px;top:2158px;font-size:38px}
.footer-about{left:88px;top:2223px;width:355px;font-size:13px;line-height:22px;color:#d7dbe2}
.socials{left:88px;top:2322px;display:flex;gap:8px}
.socials span{width:32px;height:32px;border-radius:50%;background:#2f3a4f;display:block}
.col h5{font-family:'Ubuntu',sans-serif;font-weight:500;font-size:21px;color:var(--white);margin-bottom:14px}
.col li{list-style:none;font-size:15.5px;color:var(--white);line-height:32px}
.contact li{position:relative;padding-left:28px;line-height:22px;margin-bottom:10px}
.contact li svg{position:absolute;left:0;top:2px}
.contact b{font-weight:700}
.contact .map{color:var(--green);font-weight:700;text-decoration:underline}
.foot-rule{left:88px;width:1024px;top:2434px;height:1px;background:#36415a}
.legal{top:2450px;font-size:15.5px;color:var(--white)}
</style>
</head>
<body>

<svg class="hero-bg" width="1200" height="350" aria-hidden="true"><polygon points="0,0 1200,0 1200,216 0,346" fill="var(--blue)"/></svg>

<header class="site-header">
  <div class="abs brand">Zorvel Consulting</div>
  <nav class="abs nav">
    <a>Home</a><a class="active">About Us</a><a>Our Solutions</a><a>Testimonials</a><a>Case Studies</a><a>Blog</a>
    <a class="cta">Contact Us</a>
  </nav>
</header>

<h1 class="abs page-title">About Us</h1>
<div class="abs breadcrumb">
  <svg width="18" height="16" viewBox="0 0 18 16"><path d="M9 1 1 8h2.5v7h4v-5h3v5h4V8H17z" fill="#fff"/></svg>Home<span class="sep">|</span>About Us
</div>

<div class="abs art" role="img" aria-label="Illustration of a person arranging social media tiles on a large desktop monitor" style="left:150px;top:372px;width:375px;height:370px;background:radial-gradient(circle at 45% 50%,#5ec8f5 0%,#a9e4fb 55%,#eaf8ff 100%)"></div>

<section class="abs" style="left:577px;top:484px;width:535px">
  <h2 class="section-title">WHAT WE DO</h2>
  <span class="bar" style="margin-top:10px"></span>
  <p class="copy" style="margin-top:24px">Attracting and retaining the right talent is one of the biggest challenges in any type of business in Australia.&nbsp; Zorvel consulting is transforming the management of on-demand IT talent. Our dedicated consultancy team focuses solely on IT and emerging technologies and they can help you meet your complex project requirements.</p>
</section>

<div class="abs rule" style="top:817px"></div>

<section>
  <div class="abs" style="left:0;width:1200px;top:862px;text-align:center">
    <h2 class="section-title">HOW WE DO IT</h2>
    <span class="bar" style="margin:8px auto 0"></span>
  </div>
  <div class="abs feature" style="left:68px;top:965px">
    <div class="icon"><svg width="52" height="44" viewBox="0 0 52 44" fill="var(--blue)"><circle cx="10" cy="7" r="5"/><circle cx="26" cy="5" r="5"/><circle cx="42" cy="7" r="5"/><rect x="4" y="14" width="12" height="16" rx="3"/><rect x="36" y="14" width="12" height="16" rx="3"/><rect x="19" y="12" width="14" height="20" rx="3"/><rect x="21" y="30" width="4" height="12"/><rect x="27" y="30" width="4" height="12"/><rect x="7" y="28" width="3" height="10"/><rect x="42" y="28" width="3" height="10"/></svg></div>
    <h3>we are experts</h3>
    <p>Our founders are from the IT industry.</p>
  </div>
  <div class="abs feature" style="left:286px;top:965px">
    <div class="icon"><svg width="42" height="42" viewBox="0 0 42 42" fill="none" stroke="var(--blue)" stroke-width="4"><circle cx="10" cy="21" r="6"/><circle cx="31" cy="9" r="6"/><circle cx="31" cy="33" r="6"/><path d="M15 18 26 12M15 24l11 6"/></svg></div>
    <h3>we are social</h3>
    <p>We are active on all social media platforms</p>
  </div>
  <div class="abs feature" style="left:505px;top:965px">
    <div class="icon"><svg width="58" height="40" viewBox="0 0 58 40"><path d="M14 36a11 11 0 0 1-1-22 14 14 0 0 1 27-4 11 11 0 0 1 5 26z" fill="var(--blue)"/><path d="M22 30V20M29 30V14M36 30V22" stroke="#fff" stroke-width="2"/><circle cx="22" cy="18" r="2.5" fill="#fff"/><circle cx="29" cy="12" r="2.5" fill="#fff"/><circle cx="36" cy="20" r="2.5" fill="#fff"/></svg></div>
    <h3>we are tech</h3>
    <p>we use the latest in secure Cloud based technologies</p>
  </div>
  <div class="abs feature" style="left:723px;top:965px">
    <div class="icon"><svg width="50" height="48" viewBox="0 0 50 48" fill="var(--blue)"><ellipse cx="20" cy="8" rx="18" ry="6"/><path d="M2 13c0 4 8 7 18 7s18-3 18-7v7c0 4-8 7-18 7S2 24 2 20z"/><path d="M2 25c0 4 8 7 18 7 3 0 6 0 8-1v8c-2 1-5 1-8 1-10 0-18-3-18-7z"/><circle cx="39" cy="37" r="8"/><circle cx="39" cy="37" r="3" fill="var(--blue-soft)"/></svg></div>
    <h3>we love data</h3>
    <p>we know how to use data to find the best talent in the market</p>
  </div>
  <div class="abs feature" style="left:941px;top:965px">
    <div class="icon"><svg width="52" height="56" viewBox="0 0 52 56"><path d="M26 12a13 13 0 0 0-8 23v6h16v-6a13 13 0 0 0-8-23z" fill="var(--blue)"/><rect x="19" y="43" width="14" height="4" rx="1" fill="var(--blue)"/><rect x="21" y="49" width="10" height="4" rx="1" fill="var(--blue)"/><path d="M26 1v6M9 8l4 4M43 8l-4 4M3 24h6M43 24h6M6 38l4-3M46 38l-4-3" stroke="var(--blue)" stroke-width="2.5" stroke-linecap="round"/></svg></div>
    <h3>we are creative</h3>
    <p>we don't limit ourselves to traditional sourcing methodologies</p>
  </div>
</section>

<div class="abs rule" style="top:1232px"></div>

<section>
  <div class="abs" style="left:88px;top:1282px">
    <h2 class="section-title">OUR VALUES</h2>
    <span class="bar" style="margin-top:8px;margin-left:2px"></span>
  </div>
  <div class="abs value" style="top:1380px">
    <svg width="34" height="40" viewBox="0 0 34 40"><path d="M17 1 2 7v11c0 10 7 18 15 21 8-3 15-11 15-21V7z" fill="var(--blue)"/><path d="M10 20l5 5 10-11" stroke="#fff" stroke-width="3.5" fill="none" stroke-linecap="round"/></svg>
    <h4>Trust</h4>
    <p>We earn the trust of our clients and candidates through transparency, compliance and performance. We are trusted advisors and we deliver the most trusted IT talent management services in the industry.</p>
  </div>
  <div class="abs value" style="top:1528px">
    <svg width="36" height="32" viewBox="0 0 36 32"><path d="M18 31 3 16A9 9 0 0 1 18 5a9 9 0 0 1 15 11z" fill="var(--blue)"/></svg>
    <h4>Passion</h4>
    <p>We are passionate about what we do. We are passionate about achieving our clients’ goals.</p>
  </div>
  <div class="abs value" style="top:1618px">
    <svg width="34" height="34" viewBox="0 0 34 34"><circle cx="17" cy="17" r="16" fill="var(--blue)"/><path d="M9 17l6 6 11-12" stroke="#fff" stroke-width="3.5" fill="none" stroke-linecap="round"/></svg>
    <h4>success</h4>
    <p>We help our clients achieve their goals so that we can grow together. Their success is our success</p>
  </div>
  <div class="abs art" role="img" aria-label="Illustration of a person with a megaphone beside a large phone showing a bar chart, with chat and cloud icons" style="left:642px;top:1290px;width:470px;height:405px;background:radial-gradient(circle at 55% 50%,#3b63c9 0%,#6fd3f2 45%,#e4f8fd 100%)"></div>
</section>

<svg class="cta-bg" width="1200" height="2484" style="top:0" aria-hidden="true"><polygon points="0,1918 1200,1770 1200,2484 0,2484" fill="var(--navy)"/></svg>

<section>
  <h2 class="abs cta-title">Be A Part Of IT Consulting</h2>
  <span class="abs bar" style="left:552px;top:1965px;background:var(--white)"></span>
  <p class="abs cta-text">It is a long established fact that a reader will be distracted by the readable content of a page when looking at its layout.</p>
  <div class="abs btn">Join Us Today</div>
</section>

<footer>
  <div class="abs brand footer-brand">Zorvel Consulting</div>
  <p class="abs footer-about">But I must explain to you how all this mistaken idea of denouncing pleasure and praising pain was born and I will give you a complete account of the system, and expound the actual teachings of the great explorer of the truth</p>
  <div class="abs socials" aria-label="Social links"><span></span><span></span><span></span><span></span></div>

  <div class="abs col" style="left:495px;top:2155px">
    <h5>Quick Links</h5>
    <ul><li>Home</li><li>About Us</li><li>Services</li><li>Portfolio</li><li>Contact</li></ul>
  </div>
  <div class="abs col" style="left:668px;top:2155px">
    <h5>Services</h5>
    <ul><li>App Development</li><li>Software Support</li><li>Data Management</li><li>Network Security</li><li>Cloud Computing</li></ul>
  </div>
  <div class="abs col contact" style="left:866px;top:2155px;width:250px">
    <h5>Contact</h5>
    <ul>
      <li><svg width="18" height="20" viewBox="0 0 18 20" fill="none" stroke="#fff" stroke-width="1.5"><path d="M9 19s-7-7-7-11a7 7 0 0 1 14 0c0 4-7 11-7 11z"/><circle cx="9" cy="8" r="2.5"/></svg><b>location:</b> Level 4, 18 Harlow Lane, Brindale, 3100 (map)</li>
      <li><svg width="22" height="16" viewBox="0 0 22 16" fill="none" stroke="#fff" stroke-width="1.5"><rect x="4" y="1" width="17" height="13"/><path d="M4 1l8.5 7L21 1M0 5h3M0 9h3"/></svg><b>Email:</b> Email Us</li>
      <li><svg width="20" height="20" viewBox="0 0 20 20" fill="none" stroke="#fff" stroke-width="1.5"><path d="M4 2l3 4-2 2c1 3 4 6 7 7l2-2 4 3-2 3C9 19 1 11 2 4z"/></svg><b>Phone:</b> 03 5550 1742</li>
      <li><svg width="18" height="18" viewBox="0 0 18 18" fill="none" stroke="#fff" stroke-width="1.3"><circle cx="9" cy="9" r="8"/><ellipse cx="9" cy="9" rx="3.5" ry="8"/><path d="M1 9h16M2.5 5h13M2.5 13h13"/></svg><b>Web:</b> www.zorvelconsulting.example</li>
      <li><span class="map">View Map</span></li>
    </ul>
  </div>

  <div class="abs foot-rule"></div>
  <div class="abs legal" style="left:88px">© &nbsp;Copyright 2019 · All rights reserved</div>
  <div class="abs legal" style="left:888px">Terms &amp; Condition &nbsp;&nbsp;&nbsp; Privacy Policy</div>
</footer>

</body>
</html>
```